Design a menu for a Pizza company

I need help designing a color menu for a pizza company. It will be a 9x16" trifold menu (3-panel). I would like to include some photos of pizza, salads, subs, sandwiches, drinks, etc. (no clipart). Attached is an example of an existing menu. I need to make the menu full color. We would like to modernize this menu with full color photos like the attached sample menu. The final files should have editable files so I can edit prices and menu items as needed. I prefer CorelDraw graphics software.

Target Market(s)

General public.

Industry/Entity Type

Restaurant

Font styles to use
Sans Serif

Colors
ec1f27
fffefc
9bcb3b

Requirements
Must have
• Must have photos and editable fonts. I will need to be able to edit the contents of the menu after you provide me with the final files.
Nice to have
• It would be nice to have this menu created in CorelDraw X7 or X8.
Should not have
• Should not have clip art or low resolution photos.

```html
<!DOCTYPE html>
<html lang="en">
<head>
<meta charset="utf-8">
<title>Pizza Restaurant Menu</title>
<link rel="stylesheet" href="https://fonts.googleapis.com/css2?family=Luckiest+Guy&family=Open+Sans:ital,wght@0,400;0,600;0,700;1,400;1,600&display=swap">
<style>
  :root {
    --red: #ec1f27;
    --red-deep: #b3121a;
    --green: #3f7a1c;
    --green-dark: #1f4a0c;
    --green-light: #9bcb3b;
    --cream: #fffefc;
    --ink: #3a3a3a;
    --stage: #0f2218;
    --rule: rgba(0,0,0,0.35);
  }
  * { box-sizing: border-box; margin: 0; padding: 0; }
  html, body { width: 1200px; height: 900px; overflow: hidden; }
  body {
    background: var(--stage);
    font-family: "Open Sans", Arial, sans-serif;
    display: flex; align-items: center; justify-content: center;
  }
  .menu { display: flex; width: 1128px; height: 780px; box-shadow: 0 20px 50px rgba(0,0,0,.6); }
  .panel { width: 376px; height: 780px; position: relative; overflow: hidden; }

  /* ---------- shared ---------- */
  .section-head {
    position: relative; height: 36px; margin: 0 0 6px;
    background: var(--red); border-radius: 18px;
    display: flex; align-items: center; justify-content: center;
  }
  .section-title {
    font-family: "Luckiest Guy", "Arial Black", sans-serif;
    font-size: 27px; color: var(--green); letter-spacing: .5px;
    -webkit-text-stroke: 5px var(--cream); paint-order: stroke fill;
    line-height: 1; padding-top: 4px;
  }
  .price-list { list-style: none; }
  .price-row { display: flex; align-items: flex-end; font-size: 13.5px; line-height: 18px; }
  .price-row .leader { flex: 1; border-bottom: 1px solid var(--rule); margin: 0 2px 4px; }
  .price-row .price { text-align: right; }

  /* ---------- left panel ---------- */
  .panel-dinners {
    background: radial-gradient(ellipse at 50% 40%, #3e8a1c 0%, #2c6b12 55%, #1d4f0a 100%);
    color: var(--cream); padding: 130px 20px 0 24px;
  }
  .panel-dinners .price-row .leader { border-color: rgba(255,255,255,.45); }
  .panel-dinners .section-head { margin-left: 26px; justify-content: flex-start; padding-left: 60px; }
  .food-thumb {
    position: absolute; left: -28px; top: -6px; width: 72px; height: 46px; border-radius: 50%;
    border: 3px solid var(--cream);
  }
  .thumb-pasta { background: radial-gradient(circle at 50% 45%, #c4281a 0 45%, #e7b64a 60%, #f2f0e6 75%); }
  .thumb-shrimp { background: radial-gradient(circle at 50% 45%, #d8812b 0 50%, #b5581c 65%, #f2f0e6 78%); }
  .thumb-tenders { background: radial-gradient(circle at 50% 45%, #e3a233 0 50%, #c27a1f 65%, #f2f0e6 78%); }
  .dinner-section { margin-bottom: 16px; }
  .serving-note { text-align: center; font-style: italic; font-size: 11.5px; margin-left: 40px; }
  .dressing-label { text-align: center; font-style: italic; font-size: 8.5px; margin-left: 40px; }
  .dressing-list { text-align: center; font-style: italic; font-size: 8.5px; margin: 0 0 2px 40px; }
  .price-row .note { font-style: italic; font-size: 10.5px; margin-left: 3px; }
  .food-notice {
    position: absolute; left: 30px; right: 30px; bottom: 36px;
    text-align: center; font-style: italic; font-size: 11px; line-height: 16px;
  }

  /* ---------- middle panel ---------- */
  .panel-drinks { color: var(--ink); padding: 120px 22px 0 22px; }
  .drinks-backdrop {
    position: absolute; inset: 0;
    background:
      radial-gradient(ellipse at 40% 10%, rgba(210,200,185,.55), transparent 45%),
      radial-gradient(ellipse at 60% 75%, rgba(240,215,170,.5), transparent 50%),
      linear-gradient(#f4f3f0, #efeeea);
  }
  .drinks-content { position: relative; }
  .drink-section { margin-bottom: 14px; }
  .size-head { display: flex; justify-content: flex-end; font-style: italic; font-size: 10px; color: var(--red); }
  .size-head span, .sizes span { width: 42px; text-align: right; }
  .sizes { display: flex; }
  .sub-head {
    text-align: center; font-weight: 700; font-size: 12.5px; color: var(--green-dark);
    margin: 4px 0 2px;
  }
  .panel-drinks .price-row { line-height: 17.5px; }

  /* ---------- right panel ---------- */
  .panel-cover {
    background: radial-gradient(ellipse at 50% 45%, #ee2a2f 0%, #d51a21 60%, #b3121a 100%);
    color: var(--cream);
  }
  .cover-art { position: absolute; inset: 0; }
  .brand-title {
    position: absolute; top: 28px; left: 0; right: 0; text-align: center;
    font-family: "Luckiest Guy", "Arial Black", sans-serif; color: var(--green); line-height: .9;
    -webkit-text-stroke: 8px var(--cream); paint-order: stroke fill;
  }
  .brand-title .big { display: block; font-size: 96px; letter-spacing: 2px; }
  .brand-title .small { display: block; font-size: 30px; -webkit-text-stroke-width: 5px; }
  .hours {
    position: absolute; left: 0; right: 0; bottom: 44px; text-align: center;
    font-weight: 600; font-size: 13.5px; line-height: 17px;
  }
  .hours .cards { font-weight: 400; font-size: 11.5px; }
</style>
</head>
<body>
<main class="menu">

  <!-- Dinners -->
  <section class="panel panel-dinners">
    <div class="dinner-section">
      <div class="section-head">
        <div class="food-thumb thumb-pasta" role="img" aria-label="Photo of spaghetti with meatballs"></div>
        <h2 class="section-title">Italian Dinners</h2>
      </div>
      <p class="serving-note">Served on Garlic Bread &amp; Salad</p>
      <p class="dressing-label">Choice of Dressing:</p>
      <p class="dressing-list">Ranch - French - Italian - Blue Cheese - Thousand Island</p>
      <ul class="price-list">
        <li class="price-row"><span>Spaghetti with Meat Sauce</span><span class="leader"></span><span class="price">8.99</span></li>
        <li class="price-row"><span>Spaghetti with Meatballs</span><span class="leader"></span><span class="price">9.99</span></li>
        <li class="price-row"><span>Veal Parmigiana with Spaghetti</span><span class="leader"></span><span class="price">9.99</span></li>
        <li class="price-row"><span>Chicken Parmigiana with Spaghetti</span><span class="leader"></span><span class="price">9.99</span></li>
        <li class="price-row"><span>Eggplant Parmigiana with Spaghetti</span><span class="leader"></span><span class="price">9.99</span></li>
        <li class="price-row"><span>Baked Lasagna</span><span class="leader"></span><span class="price">9.99</span></li>
        <li class="price-row"><span>Ravioli with Meat Sauce</span><span class="leader"></span><span class="price">9.99</span></li>
      </ul>
    </div>

    <div class="dinner-section">
      <div class="section-head">
        <div class="food-thumb thumb-shrimp" role="img" aria-label="Photo of fried shrimp"></div>
        <h2 class="section-title">Seafood Dinners</h2>
      </div>
      <p class="serving-note">Served on Garlic Bread, French Fries &amp; Salad</p>
      <p class="dressing-label">Choice of Dressing:</p>
      <p class="dressing-list">Ranch - French - Italian - Blue Cheese - Thousand Island</p>
      <ul class="price-list">
        <li class="price-row"><span>Shrimp Basket</span><span class="leader"></span><span class="price">8.99</span></li>
        <li class="price-row"><span>Crab Cake</span><span class="leader"></span><span class="price">10.99</span></li>
        <li class="price-row"><span>Fish Fillet</span><span class="leader"></span><span class="price">10.99</span></li>
      </ul>
    </div>

    <div class="dinner-section">
      <div class="section-head">
        <div class="food-thumb thumb-tenders" role="img" aria-label="Photo of chicken tenders"></div>
        <h2 class="section-title">Children's Menu</h2>
      </div>
      <ul class="price-list">
        <li class="price-row"><span>Chicken Tenders with French Fries</span><span class="leader"></span><span class="price">5.99</span></li>
        <li class="price-row"><span>Spaghetti with Meat Sauce</span><span class="leader"></span><span class="price">5.99</span></li>
        <li class="price-row"><span>Ravioli with Meat Sauce</span><span class="leader"></span><span class="price">5.99</span></li>
        <li class="price-row"><span>Shrimp with French Fries</span><span class="leader"></span><span class="price">5.99</span></li>
        <li class="price-row"><span>*Cheeseburger<span class="note">w/ French Fries &amp; Small Beverage</span></span><span class="leader"></span><span class="price">5.99</span></li>
      </ul>
    </div>

    <p class="food-notice">*These items are cooked to order. Consuming raw or undercooked meats may increase your risk of foodborne illness.</p>
  </section>

  <!-- Drinks -->
  <section class="panel panel-drinks">
    <div class="drinks-backdrop" role="img" aria-label="Faded photo of pizza behind the drinks list"></div>
    <div class="drinks-content">
      <div class="drink-section">
        <div class="section-head"><h2 class="section-title">Soda</h2></div>
        <ul class="price-list">
          <li class="price-row"><span>Pitcher</span><span class="leader"></span><span class="price">3.99</span></li>
        </ul>
        <div class="size-head" style="margin-top:6px"><span>12 oz.</span><span>16 oz.</span><span>24 oz.</span><span>32 oz.</span></div>
        <ul class="price-list">
          <li class="price-row"><span>Fizz Cola</span><span class="leader"></span><span class="sizes"><span>0.99</span><span>1.30</span><span>1.69</span><span>1.99</span></span></li>
          <li class="price-row"><span>Lemon Spark</span><span class="leader"></span><span class="sizes"><span>0.99</span><span>1.30</span><span>1.69</span><span>1.99</span></span></li>
          <li class="price-row"><span>Root Beer</span><span class="leader"></span><span class="sizes"><span>0.99</span><span>1.30</span><span>1.69</span><span>1.99</span></span></li>
          <li class="price-row"><span>Diet Fizz</span><span class="leader"></span><span class="sizes"><span>0.99</span><span>1.30</span><span>1.69</span><span>1.99</span></span></li>
        </ul>
      </div>

      <div class="drink-section">
        <div class="section-head"><h2 class="section-title">Beverages</h2></div>
        <div class="size-head"><span>16 oz.</span><span>24 oz.</span><span>32 oz.</span></div>
        <ul class="price-list">
          <li class="price-row"><span>Iced Tea</span><span class="leader"></span><span class="sizes"><span>1.30</span><span>1.69</span><span>1.99</span></span></li>
        </ul>
      </div>

      <div class="drink-section">
        <div class="section-head"><h2 class="section-title">Beer</h2></div>
        <h3 class="sub-head">DRAFT</h3>
        <ul class="price-list">
          <li class="price-row"><span>32 Oz. Pitcher</span><span class="leader"></span><span class="price">6.99</span></li>
          <li class="price-row"><span>60 Oz. Pitcher</span><span class="leader"></span><span class="price">10.99</span></li>
          <li class="price-row"><span>Bridgewater</span><span class="leader"></span><span class="price">2.60</span></li>
        </ul>
        <h3 class="sub-head">BOTTLES</h3>
        <ul class="price-list">
          <li class="price-row"><span>Bridgewater</span><span class="leader"></span><span class="price">3.25</span></li>
          <li class="price-row"><span>Millbrook</span><span class="leader"></span><span class="price">3.25</span></li>
          <li class="price-row"><span>Millbrook Lite</span><span class="leader"></span><span class="price">3.25</span></li>
          <li class="price-row"><span>Cordell's</span><span class="leader"></span><span class="price">3.25</span></li>
          <li class="price-row"><span>Cordell's Lite</span><span class="leader"></span><span class="price">3.25</span></li>
        </ul>
        <h3 class="sub-head">IMPORTED BOTTLES</h3>
        <ul class="price-list">
          <li class="price-row"><span>Hollander</span><span class="leader"></span><span class="price">3.75</span></li>
          <li class="price-row"><span>Costa Clara</span><span class="leader"></span><span class="price">3.75</span></li>
        </ul>
      </div>
    </div>
  </section>

  <!-- Cover -->
  <section class="panel panel-cover">
    <svg class="cover-art" viewBox="0 0 376 780" width="376" height="780">
      <defs>
        <radialGradient id="pizzaTone" cx="50%" cy="52%" r="60%">
          <stop offset="0" stop-color="#e0692a"/>
          <stop offset=".45" stop-color="#c8451f"/>
          <stop offset=".7" stop-color="#d99a4a"/>
          <stop offset="1" stop-color="#6b4a33"/>
        </radialGradient>
      </defs>
      <rect x="0" y="230" width="376" height="380" fill="url(#pizzaTone)" role="img" aria-label="Photo of a pepperoni pizza with tomatoes and herbs"/>
      <path d="M0 226 Q110 250 200 206 T376 176 L376 238 Q280 246 190 290 T0 316 Z"
            fill="var(--green)" stroke="var(--cream)" stroke-width="5"/>
      <text x="180" y="272" transform="rotate(-13 180 262)" text-anchor="middle"
            font-family="Luckiest Guy, Arial Black, sans-serif" font-size="27" fill="var(--cream)">DINE-IN &amp; CARRY OUT</text>
      <path d="M0 580 Q120 600 220 556 T376 512 L376 582 Q270 590 190 630 T0 660 L0 760 L0 660 Z"
            fill="var(--green)" stroke="var(--cream)" stroke-width="5"/>
      <text x="196" y="610" transform="rotate(-14 196 600)" text-anchor="middle"
            font-family="Luckiest Guy, Arial Black, sans-serif" font-size="28" fill="var(--cream)">OPEN 7 DAYS A WEEK</text>
    </svg>
    <h1 class="brand-title"><span class="big">PIZZA</span><span class="small">RESTAURANT</span></h1>
    <div class="hours">
      <p>Monday - Thursday 10:30 AM - 9:30 PM</p>
      <p>Friday - Saturday 10:30 AM - 10:00 PM</p>
      <p>Sunday 12:00 Noon - 8:00 PM</p>
      <p class="cards">Major Credit Cards Accepted</p>
    </div>
  </section>

</main>
</body>
</html>
```